Inspired and Functional Refresh for established website

Looking for homepage redesign inspiration for our existing site. It's content heavy, but not many CTAs on the front page - need it to display relevant content and most importantly, get people clicking through to our courses, membership, books and events. The existing site is voltrique.org. Colours and logo to stay as per our existing site, and our brand guidelines (attached).
Updates

Need extra days to review

Target Market(s)

Engineers

Industry/Entity Type

Engineering

Number of Pages Required

1 page

Font styles to use
Other font styles liked:
• Arial for body text, Monsterrat for headings.

Requirements
Nice to have
• We want the homepage to be visually attractive, as well as giving information on our training courses, membership, events and blog articles.

```html
<!DOCTYPE html>
<html lang="en">
<head>
<meta charset="utf-8">
<title>Voltrique – Home</title>
<link rel="stylesheet" href="https://fonts.googleapis.com/css2?family=Montserrat:wght@400;500;600;700&display=swap">
<style>
:root{
  --stage:#3a3a3b;
  --red:#e3262a;
  --ink:#1f1f21;
  --white:#ffffff;
  --sand:#f3f2ee;
  --mist:#f3f4f5;
  --olive:#dcd886;
  --hero-tone:#26303d;
  --card-tone:#cfcac1;
  --beer-tone:#e9e6e0;
  --tube-tone:#d3b27a;
  --bag-tone:#e3d3b8;
  --desk-tone:#4a372c;
  --skin-a:#b89580;
  --skin-b:#a8866f;
  --skin-c:#d7b39b;
}
*{box-sizing:border-box;margin:0;padding:0}
html,body{width:1200px;height:4232px;overflow:hidden}
body{background:var(--stage);font-family:"Montserrat",Arial,sans-serif;color:var(--ink)}
.page{position:absolute;left:108px;top:107px;width:981px;background:var(--white)}
section,footer{position:relative;width:981px;overflow:hidden}
.red{color:var(--red)}
.photo{position:absolute}

/* hero */
.hero{height:551px}
.hero-photo{inset:0;background:linear-gradient(180deg,#24303e 0%,#2e3640 60%,#2b2e30 100%)}
.brand{position:absolute;left:127px;top:54px;display:flex;align-items:center;gap:8px;color:var(--white);font-weight:700;font-size:19px;letter-spacing:.5px}
.brand-mark{width:14px;height:14px;background:var(--white)}
.nav{position:absolute;top:57px;left:0;list-style:none;color:var(--white);font-size:13.5px}
.nav li{position:absolute;white-space:nowrap}
.nav .current::after{content:"";position:absolute;left:0;right:0;top:22px;height:2px;background:var(--white)}
.hero-title{position:absolute;left:127px;top:180px;color:var(--white);font-weight:400;font-size:57px;line-height:54px;letter-spacing:1px}
.hero-lead{position:absolute;left:133px;top:312px;color:var(--white);font-size:14.5px;line-height:19px}
.btn{position:absolute;display:flex;align-items:center;justify-content:center;font-size:11.5px;color:var(--white);text-transform:uppercase}
.btn-solid{left:133px;top:398px;width:110px;height:33px;background:var(--red)}
.btn-ghost{left:260px;top:398px;width:108px;height:33px;border:2px solid var(--white)}

/* shared heading */
.section-title{position:absolute;left:132px;font-size:36px;line-height:44px;font-weight:400;text-transform:uppercase;letter-spacing:.5px}
.section-title b{display:block;color:var(--red);font-weight:700}
.copy{font-size:9.5px;line-height:14.6px;color:#55555a;text-align:justify}

/* about */
.about{height:473px}
.about .section-title{top:62px;font-size:33px;line-height:44px;letter-spacing:0}
.about .section-title b{font-size:31px}
.about-copy{position:absolute;left:132px;top:220px;width:187px;height:200px;overflow:hidden}
.about-panel{position:absolute;left:344px;top:0;width:242px;height:473px;background:var(--red)}
.pillar{position:absolute;left:25px;width:192px;color:var(--white);text-align:right}
.pillar h3{font-weight:400;font-size:23px;text-align:left;letter-spacing:.5px}
.pillar p{font-size:13px;letter-spacing:.5px;margin-top:1px}
.pillar-rule{position:absolute;left:25px;width:192px;height:1px;background:rgba(255,255,255,.55)}
.tag{position:absolute;left:568px;width:38px;height:38px;border-radius:50%;background:var(--white);border:3px solid #f7b3b1;display:flex;align-items:center;justify-content:center}
.about-note{position:absolute;left:623px;width:224px;height:58px;overflow:hidden}

/* services */
.services{height:488px;background:var(--sand)}
.services .section-title{top:297px}
.card{position:absolute;width:158px;background:var(--white);text-align:center}
.card h4{font-size:10.5px;font-weight:600;color:var(--red);text-transform:uppercase;margin-top:8px}
.card .copy{margin:3px 18px 0;height:58px;overflow:hidden}
.service-card{height:187px;padding-top:26px}
.icon{display:block;margin:0 auto;stroke:#333;fill:none;stroke-width:1.4;stroke-linecap:round;stroke-linejoin:round}

/* events */
.events{height:472px}
.events .section-title{top:286px}
.thumb{position:absolute;left:346px;width:156px;height:110px}
.date{position:absolute;left:0;bottom:0;width:32px;height:38px;background:var(--red);color:var(--white);text-align:center;font-weight:700;font-size:22px;line-height:26px}
.date small{display:block;font-size:6.5px;line-height:8px;font-weight:600}
.post{position:absolute;left:515px;width:149px}
.post h5{font-size:9px;font-weight:600;color:var(--red);line-height:11px;text-transform:uppercase}
.post .copy{margin-top:4px;height:73px;overflow:hidden}
.feature{position:absolute;left:692px;top:54px;width:158px;height:365px;background:#7d7a77}
.feature .date{top:10px;left:10px;bottom:auto}
.feature-text{position:absolute;left:6px;right:6px;bottom:4px;color:var(--white)}
.feature-text h5{font-size:9.5px;font-weight:600;line-height:11px}
.feature-text .copy{color:#f1f1f1;margin-top:4px;height:58px;overflow:hidden}

/* team */
.team{height:487px;background:var(--mist)}
.team .section-title{top:301px}
.member{position:absolute;top:49px;width:158px}
.portrait{position:relative;height:250px}
.member h4{font-size:14px;font-weight:400;text-align:center;margin-top:26px;color:#333}
.member h6{font-size:10px;font-weight:500;color:var(--red);text-align:center;margin-top:4px}
.member .copy{margin-top:8px;height:59px;overflow:hidden;color:#333}

/* portfolio */
.portfolio{height:488px}
.portfolio .section-title{left:228px;top:303px}

/* courses */
.courses{height:488px;background:var(--mist)}
.courses .section-title{top:298px}
.course-card{height:385px;top:51px;padding-top:34px}
.course-card h4{color:var(--ink);font-size:10.5px;margin-top:22px}
.course-card h6{font-size:9.5px;font-weight:500;color:var(--red);margin-top:4px}
.course-card .copy{height:117px;margin-top:13px;color:#444}
.price{font-size:36px;font-weight:700;line-height:40px;margin-top:10px;color:#333}
.course-card:nth-of-type(2) .price{color:var(--red)}
.btn-small{position:static;display:inline-flex;width:96px;height:30px;background:var(--red);font-size:10.5px;margin-top:6px}

/* find us */
.find{height:485px}
.find .section-title{top:54px}
.contact{position:absolute;left:132px;width:270px}
.contact svg{position:absolute;left:0;top:0}
.contact h4{margin-left:50px;font-size:18px;font-weight:700;color:var(--red);text-transform:uppercase}
.contact p{margin-left:50px;font-size:9.5px;line-height:13.5px;color:#333}
.desk{left:418px;top:0;width:563px;height:485px;background:var(--desk-tone)}

footer{height:87px;background:var(--mist);display:flex;align-items:center;justify-content:center;font-size:9.5px;color:#555}
</style>
</head>
<body>
<main class="page">

  <section class="hero">
    <div class="photo hero-photo" role="img" aria-label="Aerial photograph of a city skyline with motorways"></div>
    <div class="brand"><span class="brand-mark"></span>VOLTRIQUE</div>
    <ul class="nav">
      <li class="current" style="left:302px">Home</li>
      <li style="left:381px">About us</li>
      <li style="left:481px">Services</li>
      <li style="left:583px">Portfolio</li>
      <li style="left:680px">Our team</li>
      <li style="left:784px">News</li>
      <li style="left:861px">Contact</li>
    </ul>
    <h1 class="hero-title">WELCOME TO THE<br><span class="red">VOLTRIQUE</span> BRAND</h1>
    <p class="hero-lead">Lorem ipsum dolor sit amet, consectetur adipiscing elit,<br>sed do eiusmod tempor incididunt ut labore et dolore</p>
    <a class="btn btn-solid">Read more</a>
    <a class="btn btn-ghost">Read more</a>
  </section>

  <section class="about">
    <h2 class="section-title">About<b>Voltrique</b>Brand</h2>
    <p class="copy about-copy">Lorem ipsum dolor sit amet, consectetur adipiscing elit, sed do eiusmod tempor incididunt ut labore et dolore magna aliqua. Ut enim ad minim veniam, quis nostrud exercitation ullamco laboris nisi ut aliquip ex ea commodo consequat. Lorem ipsum dolor sit amet, consectetur adipiscing elit, sed do eiusmod tempor incididunt ut labore et dolore magna aliqua. Ut enim ad minim veniam, quis nostrud exercitation ullamco laboris nisi ut aliquip ex ea commodo consequat.</p>
    <div class="about-panel" role="img" aria-label="Red-tinted photograph of a person at work">
      <div class="pillar" style="top:35px"><h3>LOREM IPSUM</h3><p>LOREM IPSUM</p></div>
      <div class="pillar-rule" style="top:103px"></div>
      <div class="pillar" style="top:127px"><h3>LOREM IPSUM</h3><p>LOREM IPSUM</p></div>
      <div class="pillar-rule" style="top:210px"></div>
      <div class="pillar" style="top:229px"><h3>LOREM IPSUM</h3><p>LOREM IPSUM</p></div>
      <div class="pillar-rule" style="top:317px"></div>
      <div class="pillar" style="top:339px"><h3>LOREM IPSUM</h3><p>LOREM IPSUM</p></div>
    </div>
    <div class="tag" style="top:34px"><svg width="16" height="16" viewBox="0 0 16 16" fill="none" stroke="#e3262a" stroke-width="1.3"><path d="M2 8 8 2h6v6l-6 6z"/><circle cx="11" cy="5" r="1"/></svg></div>
    <div class="tag" style="top:134px"><svg width="16" height="16" viewBox="0 0 16 16" fill="none" stroke="#e3262a" stroke-width="1.3"><path d="M2 8 8 2h6v6l-6 6z"/><circle cx="11" cy="5" r="1"/></svg></div>
    <div class="tag" style="top:236px"><svg width="16" height="16" viewBox="0 0 16 16" fill="none" stroke="#e3262a" stroke-width="1.3"><path d="M2 8 8 2h6v6l-6 6z"/><circle cx="11" cy="5" r="1"/></svg></div>
    <div class="tag" style="top:346px"><svg width="16" height="16" viewBox="0 0 16 16" fill="none" stroke="#e3262a" stroke-width="1.3"><path d="M2 8 8 2h6v6l-6 6z"/><circle cx="11" cy="5" r="1"/></svg></div>
    <p class="copy about-note" style="top:32px">Lorem ipsum dolor sit amet, consectetur adipiscing elit, sed do eiusmod tempor incididunt ut labore et dolore magna aliqua. Ut enim ad minim veniam, quis nostrud exercita-</p>
    <p class="copy about-note" style="top:132px">Lorem ipsum dolor sit amet, consectetur adipiscing elit, sed do eiusmod tempor incididunt ut labore et dolore magna aliqua. Ut enim ad minim veniam, quis nostrud exercita-</p>
    <p class="copy about-note" style="top:234px">Lorem ipsum dolor sit amet, consectetur adipiscing elit, sed do eiusmod tempor incididunt ut labore et dolore magna aliqua. Ut enim ad minim veniam, quis nostrud exercita-</p>
    <p class="copy about-note" style="top:344px">Lorem ipsum dolor sit amet, consectetur adipiscing elit, sed do eiusmod tempor incididunt ut labore et dolore magna aliqua. Ut enim ad minim veniam, quis nostrud exercita-</p>
  </section>

  <section class="services">
    <h2 class="section-title">Our<b>Special</b>Services</h2>
    <div class="card service-card" style="left:344px;top:51px">
      <svg class="icon" width="34" height="34" viewBox="0 0 34 34"><circle cx="17" cy="17" r="13"/><ellipse cx="17" cy="17" rx="6" ry="13"/><path d="M4 17h26M6 10h22M6 24h22"/></svg>
      <h4>Achieves</h4><p class="copy">Lorem ipsum dolor sit amet, consectetur adipiscing elit, sed do eiusmod tempor incidi-</p></div>
    <div class="card service-card" style="left:518px;top:51px">
      <svg class="icon" width="34" height="34" viewBox="0 0 34 34"><path d="M10 23a6 6 0 0 1 0-12 8 8 0 0 1 15 2 5 5 0 0 1 0 10h-3"/><path d="M17 15v14M13 25l4 4 4-4"/></svg>
      <h4>Designer</h4><p class="copy">Lorem ipsum dolor sit amet, consectetur adipiscing elit, sed do eiusmod tempor incidi-</p></div>
    <div class="card service-card" style="left:692px;top:51px">
      <svg class="icon" width="34" height="34" viewBox="0 0 34 34"><rect x="6" y="8" width="22" height="20"/><path d="M6 14h22M14 8v6M20 8v6M17 18v6M14 21l3-3 3 3"/></svg>
      <h4>Perfect design</h4><p class="copy">Lorem ipsum dolor sit amet, consectetur adipiscing elit, sed do eiusmod tempor incidi-</p></div>
    <div class="card service-card" style="left:344px;top:250px">
      <svg class="icon" width="34" height="34" viewBox="0 0 34 34"><path d="M4 17a13 10 0 0 1 26 0c-2-2-5-2-6.5 0-1.5-2-5-2-6.5 0-1.5-2-5-2-6.5 0-1.5-2-4.5-2-6.5 0z"/><path d="M17 17v10a2.5 2.5 0 0 1-5 0"/></svg>
      <h4>Perfect design</h4><p class="copy">Lorem ipsum dolor sit amet, consectetur adipiscing elit, sed do eiusmod tempor incidi-</p></div>
    <div class="card service-card" style="left:518px;top:250px">
      <svg class="icon" width="34" height="34" viewBox="0 0 34 34"><path d="M24 18v11H6V9h11"/><path d="M14 21l1-5L26 5l4 4-11 11z"/></svg>
      <h4>Achieves</h4><p class="copy">Lorem ipsum dolor sit amet, consectetur adipiscing elit, sed do eiusmod tempor incidi-</p></div>
    <div class="card service-card" style="left:692px;top:250px">
      <svg class="icon" width="34" height="34" viewBox="0 0 34 34"><path d="M13 18V6a2 2 0 0 1 4 0v10l8 2a3 3 0 0 1 2 3v5l-3 5H14l-5-8a2 2 0 0 1 3-3l1 2"/></svg>
      <h4>Achieves</h4><p class="copy">Lorem ipsum dolor sit amet, consectetur adipiscing elit, sed do eiusmod tempor incidi-</p></div>
  </section>

  <section class="events">
    <h2 class="section-title">Latest<b>Events</b>Blog</h2>
    <div class="thumb" style="top:51px;background:#d9c7a4" role="img" aria-label="Photograph of a gold robot figurine on a desk"><div class="date">24<small>DEC,18</small></div></div>
    <div class="thumb" style="top:178px;background:#7fa3c2" role="img" aria-label="Photograph of a man in a cap against a blue sky"><div class="date">24<small>DEC,18</small></div></div>
    <div class="thumb" style="top:307px;background:#6e4a35" role="img" aria-label="Photograph of a bookshelf with a laptop on a desk"><div class="date">24<small>DEC,18</small></div></div>
    <div class="post" style="top:51px"><h5>Designed and built with care</h5><p class="copy">Lorem ipsum dolor sit amet, consectetur adipiscing elit, sed do eiusmod tempor incididunt ut labore et dolore magna aliqua. Ut enim ad</p></div>
    <div class="post" style="top:180px"><h5>Designed and built with care</h5><p class="copy">Lorem ipsum dolor sit amet, consectetur adipiscing elit, sed do eiusmod tempor incididunt ut labore et dolore magna aliqua. Ut enim ad</p></div>
    <div class="post" style="top:309px"><h5>Designed and built with care</h5><p class="copy">Lorem ipsum dolor sit amet, consectetur adipiscing elit, sed do eiusmod tempor incididunt ut labore et dolore magna aliqua. Ut enim ad</p></div>
    <div class="feature" role="img" aria-label="Photograph of a musician playing guitar on a city street">
      <div class="date">24<small>DEC,18</small></div>
      <div class="feature-text"><h5>DESIGNED AND BUILT WITH CARE</h5><p class="copy">Lorem ipsum dolor sit amet, consectetur adipiscing elit, sed do eiusmod tempor incididunt ut labore et dolore magna aliqua. Ut enim ad</p></div>
    </div>
  </section>

  <section class="team">
    <h2 class="section-title">Creative<b>Team</b>Members</h2>
    <div class="member" style="left:344px"><div class="portrait" role="img" aria-label="Portrait photograph of a team member" style="background:var(--skin-a)"></div><h4>DESIGNER NAME</h4><h6>GRAPHIC DESIGNER</h6><p class="copy">Lorem ipsum dolor sit amet, consectetur adipiscing elit, sed do eiusmod tempor incididunt ut labore et dolore</p></div>
    <div class="member" style="left:518px"><div class="portrait" role="img" aria-label="Portrait photograph of a team member" style="background:var(--skin-b)"></div><h4>DESIGNER NAME</h4><h6>GRAPHIC DESIGNER</h6><p class="copy">Lorem ipsum dolor sit amet, consectetur adipiscing elit, sed do eiusmod tempor incididunt ut labore et dolore</p></div>
    <div class="member" style="left:692px"><div class="portrait" role="img" aria-label="Portrait photograph of a team member" style="background:var(--skin-c)"></div><h4>DESIGNER NAME</h4><h6>GRAPHIC DESIGNER</h6><p class="copy">Lorem ipsum dolor sit amet, consectetur adipiscing elit, sed do eiusmod tempor incididunt ut labore et dolore</p></div>
  </section>

  <section class="portfolio">
    <div class="photo" style="left:0;top:0;width:490px;height:163px;background:var(--card-tone)" role="img" aria-label="Mockup of business cards on a wooden table"></div>
    <div class="photo" style="left:490px;top:0;width:491px;height:163px;background:var(--olive)" role="img" aria-label="Mockup of a folded newspaper"></div>
    <div class="photo" style="left:0;top:163px;width:196px;height:325px;background:var(--beer-tone)" role="img" aria-label="Mockup of a beer glass and bottle"></div>
    <h2 class="section-title">Our<b>Portfolio</b>Gallery</h2>
    <div class="photo" style="left:490px;top:163px;width:244px;height:163px;background:var(--tube-tone)" role="img" aria-label="Mockup of a gold and kraft paper tube"></div>
    <div class="photo" style="left:490px;top:326px;width:244px;height:162px;background:var(--olive)" role="img" aria-label="Mockup of a branded paper coffee cup"></div>
    <div class="photo" style="left:734px;top:163px;width:247px;height:325px;background:var(--bag-tone)" role="img" aria-label="Mockup of a kraft paper coffee bag with a red label"></div>
  </section>

  <section class="courses">
    <h2 class="section-title">Our<b>Courses</b>Package</h2>
    <div class="card course-card" style="left:344px">
      <svg class="icon" width="42" height="46" viewBox="0 0 42 46"><path d="M14 30c0-5-7-8-7-16a14 14 0 0 1 28 0c0 8-7 11-7 16z"/><path d="M15 34h12M16 38h10M18 42h6M21 30V18M17 16l4 3 4-3"/></svg>
      <h4>DESIGNER NAME</h4><h6>GRAPHIC DESIGNER</h6>
      <p class="copy">Lorem ipsum dolor sit amet, consectetur adipiscing elit, sed do eiusmod tempor incididunt ut labore et dolore magna aliqua. Ut enim ad minim veniam, quis nostrud exercitation ullamco</p>
      <div class="price">$50</div><a class="btn btn-small">Read more</a></div>
    <div class="card course-card" style="left:518px">
      <svg class="icon" width="54" height="46" viewBox="0 0 54 46"><path d="M4 4h8l6 26h26l5-18H15"/><circle cx="21" cy="39" r="3.5"/><circle cx="40" cy="39" r="3.5"/></svg>
      <h4>DESIGNER NAME</h4><h6>GRAPHIC DESIGNER</h6>
      <p class="copy">Lorem ipsum dolor sit amet, consectetur adipiscing elit, sed do eiusmod tempor incididunt ut labore et dolore magna aliqua. Ut enim ad minim veniam, quis nostrud exercitation ullamco</p>
      <div class="price">$500</div><a class="btn btn-small">Read more</a></div>
    <div class="card course-card" style="left:692px">
      <svg class="icon" width="56" height="46" viewBox="0 0 56 46"><rect x="12" y="4" width="38" height="30" rx="2"/><path d="M6 12v30h38"/><circle cx="38" cy="13" r="4"/><path d="M14 32l12-12 10 10 5-5 9 9"/></svg>
      <h4>DESIGNER NAME</h4><h6>GRAPHIC DESIGNER</h6>
      <p class="copy">Lorem ipsum dolor sit amet, consectetur adipiscing elit, sed do eiusmod tempor incididunt ut labore et dolore magna aliqua. Ut enim ad minim veniam, quis nostrud exercitation ullamco</p>
      <div class="price">$1000</div><a class="btn btn-small">Read more</a></div>
  </section>

  <section class="find">
    <h2 class="section-title">How<b>Find us</b></h2>
    <div class="contact" style="top:182px">
      <svg class="icon" width="30" height="32" viewBox="0 0 30 32"><path d="M15 28s-9-9-9-16a9 9 0 0 1 18 0c0 7-9 16-9 16z"/><circle cx="15" cy="12" r="3.5"/><path d="M3 30h24"/></svg>
      <h4>Address</h4><p>Larkfield House - Mere Court<br>Halden Road, Ashbury<br>AB12 3CD, United Kingdom</p></div>
    <div class="contact" style="top:270px">
      <svg class="icon" width="30" height="32" viewBox="0 0 30 32"><path d="M6 4l5 0 3 7-3 2a16 16 0 0 0 8 8l2-3 7 3v5a3 3 0 0 1-3 3C13 29 3 19 3 7a3 3 0 0 1 3-3z"/><path d="M19 4a9 9 0 0 1 8 8M18 9a4 4 0 0 1 4 4"/></svg>
      <h4>Call us</h4><p>+44 1632 96 04 17</p></div>
    <div class="contact" style="top:344px">
      <svg class="icon" width="30" height="32" viewBox="0 0 30 32"><rect x="3" y="10" width="24" height="17"/><path d="M3 10l12 9 12-9M8 10V5h14v5"/></svg>
      <h4>Email</h4><p>accounts@voltrique.org</p></div>
    <div class="contact" style="top:410px">
      <svg class="icon" width="30" height="32" viewBox="0 0 30 32"><rect x="3" y="5" width="24" height="17"/><path d="M3 18h24M12 22l-1 5h8l-1-5M9 28h12"/></svg>
      <h4>Website</h4><p>www.voltrique.org</p></div>
    <div class="photo desk" role="img" aria-label="Photograph of a laptop on a wooden desk with a white chair"></div>
  </section>

  <footer>Copyright © 2023.</footer>
</main>
</body>
</html>
```